New email newsletter banner needed

Financial services firm need a new banner for a newsletter banner. The old one attached.... Size is 4cm x 16cm and should read "Looking for Options".

Base colors can be Pantone colors 281,644,425,1805,405 and any gradient of those.

Font should be Arial MT

Please note the firm mentioned in the old banner no longer applies

Financial

• images of people, multiple images

```html
<!DOCTYPE html>
<html lang="en">
<head>
<meta charset="utf-8">
<title>Looking for Options – Newsletter Banner</title>
<link rel="stylesheet" href="https://fonts.googleapis.com/css2?family=Arimo:wght@400&display=swap">
<style>
  :root {
    --navy-deep: #0f2a72;
    --navy: #1c3f96;
    --blue-mid: #2a5bb8;
    --grid-line: rgba(160, 195, 255, 0.14);
    --headline: #ffffff;
    --art-gold: #b9a56a;
    --art-green: #6f9a55;
  }
  html, body {
    margin: 0;
    padding: 0;
    width: 1200px;
    height: 299px;
    overflow: hidden;
    background: #ffffff;
  }
  .banner {
    position: relative;
    width: 1200px;
    height: 299px;
    overflow: hidden;
    background:
      radial-gradient(ellipse 520px 260px at 930px 120px, rgba(110, 160, 235, 0.45), rgba(110, 160, 235, 0) 70%),
      linear-gradient(180deg, var(--navy) 0%, var(--blue-mid) 55%, var(--navy-deep) 100%);
  }
  .banner__grid {
    position: absolute;
    inset: 0;
  }
  .banner__headline {
    position: absolute;
    left: 72px;
    top: 76px;
    margin: 0;
    font-family: "Arimo", Arial, sans-serif;
    font-weight: 400;
    font-size: 74px;
    line-height: 1;
    color: var(--headline);
    text-shadow: 0 2px 3px rgba(5, 20, 60, 0.35);
    white-space: nowrap;
  }
  .banner__art {
    position: absolute;
    left: 760px;
    top: 12px;
    width: 420px;
    height: 262px;
    border-radius: 6px;
    background: linear-gradient(180deg, var(--art-green) 0%, var(--art-gold) 100%);
    opacity: 0.85;
  }
</style>
</head>
<body>
  <div class="banner">
    <svg class="banner__grid" width="1200" height="299" viewBox="0 0 1200 299" aria-hidden="true">
      <g stroke="var(--grid-line)" stroke-width="1">
        <line x1="0" y1="50" x2="1200" y2="50"/>
        <line x1="0" y1="100" x2="1200" y2="100"/>
        <line x1="0" y1="150" x2="1200" y2="150"/>
        <line x1="0" y1="200" x2="1200" y2="200"/>
        <line x1="0" y1="250" x2="1200" y2="250"/>
        <line x1="150" y1="0" x2="150" y2="299"/>
        <line x1="300" y1="0" x2="300" y2="299"/>
        <line x1="450" y1="0" x2="450" y2="299"/>
        <line x1="600" y1="0" x2="600" y2="299"/>
        <line x1="750" y1="0" x2="750" y2="299"/>
        <line x1="900" y1="0" x2="900" y2="299"/>
        <line x1="1050" y1="0" x2="1050" y2="299"/>
      </g>
    </svg>

    <h1 class="banner__headline">Looking for Options</h1>

    <div class="banner__art" role="img"
         aria-label="Illustration area: a pile of coins with a young green sprout growing out of it"></div>
  </div>
</body>
</html>
```